Ridgeline Sawcutting, Inc. Business Card

Create a business card that is eye catching and based around concrete sawcutting. I've attached our current business card and logo for reference. We like aspects of the current business card, but it is starting to feel very loud and lost. We would like something that is still fun but is more modern and streamlined.

```html
<!DOCTYPE html>
<html lang="en">
<head>
<meta charset="utf-8">
<title>Ridgeline Sawcutting, Inc. Business Card</title>
<link rel="stylesheet" href="https://fonts.googleapis.com/css2?family=Open+Sans:wght@400;600;700&display=swap">
<style>
  :root {
    --backdrop: #2b2b2f;
    --card: #1d1d21;
    --card-deep: #16161a;
    --red: #e3151f;
    --yellow: #f6d31a;
    --white: #f4f4f4;
    --pattern-a: #26262b;
    --pattern-b: #1a1a1e;
  }
  * { box-sizing: border-box; margin: 0; padding: 0; }
  html, body { width: 1200px; height: 780px; overflow: hidden; }
  body {
    background: var(--backdrop);
    font-family: "Open Sans", Arial, sans-serif;
    display: flex;
    align-items: center;
    justify-content: center;
    gap: 40px;
  }
  .card {
    position: relative;
    width: 540px;
    height: 309px;
    border-radius: 22px;
    background: var(--card);
    border-bottom: 5px solid var(--red);
    border-left: 2px solid var(--red);
    overflow: hidden;
    box-shadow: 0 18px 40px rgba(0,0,0,.45);
  }
  /* Back */
  .card-back__texture {
    position: absolute; inset: 0;
    background: radial-gradient(circle at 40% 40%, var(--pattern-a), var(--pattern-b));
  }
  .card-back__mark {
    position: absolute; top: 22px; right: 26px;
    display: flex; align-items: center; gap: 7px;
    color: var(--white); font-size: 10px; font-weight: 700;
  }
  .mark-dot {
    width: 12px; height: 12px; border-radius: 50%; background: var(--red);
  }
  /* Front */
  .card-front__name {
    position: absolute; top: 24px; right: 40px;
    font-size: 26px; font-weight: 700; letter-spacing: .5px;
  }
  .name-first { color: var(--red); }
  .name-last { color: var(--yellow); }
  .card-front__tab {
    position: absolute; top: 26px; right: 0;
    width: 22px; height: 28px; background: var(--red);
  }
  .services {
    position: absolute; top: 92px; right: 26px;
    list-style: none; text-align: right;
    font-size: 12.5px; line-height: 19px; color: var(--white);
  }
  .services__title { color: var(--red); font-weight: 700; font-size: 14px; }
  .services li::after {
    content: ""; display: inline-block; width: 7px; height: 7px;
    border-radius: 50%; margin-left: 8px; vertical-align: 1px;
  }
  .services li:nth-child(odd)::after { background: var(--red); }
  .services li:nth-child(even)::after { background: var(--yellow); }
  .brand {
    position: absolute; top: 94px; left: 28px;
    display: flex; align-items: center; gap: 10px;
    color: var(--white); font-size: 15px; font-weight: 700;
  }
  .brand .mark-dot { width: 18px; height: 18px; }
  .address {
    position: absolute; left: 28px; top: 150px;
    color: var(--white); font-size: 12.5px; line-height: 18px;
  }
  .contact {
    position: absolute; left: 28px; top: 196px;
    list-style: none; color: var(--white);
    font-size: 12.5px; line-height: 20px;
  }
  .contact li { display: flex; align-items: center; gap: 9px; }
  .contact svg { width: 13px; height: 13px; flex: none; }
</style>
</head>
<body>
  <section class="card card-back" aria-label="Card back">
    <div class="card-back__texture" role="img" aria-label="Repeating tonal emblem pattern across the card back"></div>
    <div class="card-back__mark"><span class="mark-dot"></span>Ridgeline Sawcutting, Inc.</div>
  </section>

  <section class="card card-front" aria-label="Card front">
    <h1 class="card-front__name"><span class="name-first">MARISSA</span> <span class="name-last">DELGADO</span></h1>
    <span class="card-front__tab"></span>

    <ul class="services">
      <li class="services__title">OUR SERVICES</li>
      <li>WALL SAWING</li>
      <li>CORE DRILLING</li>
      <li>SLAB SAWING</li>
      <li>BREAKING &amp; REMOVAL</li>
    </ul>

    <div class="brand"><span class="mark-dot"></span>Ridgeline Sawcutting, Inc.</div>

    <p class="address">48 Orchard Hill Rd.<br>Fairbrook, NJ 07100</p>

    <ul class="contact">
      <li>
        <svg viewBox="0 0 16 16"><path fill="var(--red)" d="M3.5 1.5l2.5 0 1 3.5-1.6 1.2a8 8 0 0 0 4.4 4.4L11 9l3.5 1v2.5c0 1-1 2-2 2A11 11 0 0 1 1.5 3.5c0-1 1-2 2-2z"/></svg>
        855.555.0148 (Office)
      </li>
      <li>
        <svg viewBox="0 0 16 16"><rect x="4" y="1" width="8" height="14" rx="1.5" fill="none" stroke="var(--yellow)" stroke-width="1.6"/></svg>
        973.555.0172 (Cell)
      </li>
      <li>
        <svg viewBox="0 0 16 16"><circle cx="8" cy="8" r="6.5" fill="none" stroke="var(--red)" stroke-width="1.6"/><path d="M1.5 8h13M8 1.5c-3 3.5-3 9.5 0 13M8 1.5c3 3.5 3 9.5 0 13" fill="none" stroke="var(--red)" stroke-width="1.2"/></svg>
        www.RidgelineSawcutting.com
      </li>
      <li>
        <svg viewBox="0 0 16 16"><rect x="1" y="3.5" width="14" height="9.5" rx="1" fill="none" stroke="var(--yellow)" stroke-width="1.6"/><path d="M1.5 4l6.5 5 6.5-5" fill="none" stroke="var(--yellow)" stroke-width="1.4"/></svg>
        marissa@RidgelineSawcutting.com
      </li>
    </ul>
  </section>
</body>
</html>
```